CoralPathway background design

The task is to create a modern looking and very attractive background for the coralPathway laboratory results reports + cover-page for the reports that matches the same design.

The background should be beautiful but also minimalistic enough not to interfere with the content inside the reports. If the background behind the content is too intensive then it is difficult to read the content. Our LOGO is blue and we have used blue-ish colors so far so perhaps one should try to keep blue at least as one of the colors. We have preferred to keep the design abstract/minimalistic rather than using photos.

Please look at the attached files, especially the file "Report with the current background" where you will see how the content is layed inside the reports. You will also see the current background that we would like to change. Then there is a file that contains the report pages without background that you could use to present the background.

```html
<!DOCTYPE html>
<html lang="en">
<head>
<meta charset="utf-8">
<title>CoralPathway – Doctor's Summary</title>
<link rel="stylesheet" href="https://fonts.googleapis.com/css2?family=Open+Sans:wght@300;400;600;700&display=swap">
<style>
  :root {
    --brand-blue: #1aa9e3;
    --ink: #555a5f;
    --ink-strong: #3f4448;
    --rule: #cfd2d5;
    --ok: #22a657;
    --alert: #e3262b;
    --band-cyan: #a9eef5;
    --band-lilac: #c9cde3;
    --band-blue: #7f9ee6;
    --band-green: #2fae6e;
    --page: #ffffff;
  }
  * { box-sizing: border-box; margin: 0; padding: 0; }
  html, body { width: 848px; height: 1200px; overflow: hidden; background: var(--page); }
  body { position: relative; font-family: "Open Sans", Arial, sans-serif; color: var(--ink); }

  .band { position: absolute; left: 0; width: 848px; }
  .band--top {
    top: 0; height: 57px;
    background: linear-gradient(100deg, var(--band-cyan) 0%, #dff7fb 22%, var(--band-lilac) 45%, var(--band-blue) 78%, var(--band-green) 100%);
  }
  .band--bottom {
    bottom: 0; height: 60px;
    background: linear-gradient(100deg, var(--band-green) 0%, var(--band-blue) 14%, var(--band-lilac) 45%, #dff7fb 75%, var(--band-cyan) 100%);
  }

  .brand {
    position: absolute; top: 58px; left: 0; width: 848px;
    display: flex; justify-content: center; align-items: center; gap: 8px;
    color: var(--brand-blue); font-size: 21px; font-weight: 400; padding-left: 40px;
  }
  .brand__dot { width: 18px; height: 18px; border-radius: 50%; background: var(--brand-blue); }

  .title {
    position: absolute; left: 61px; top: 193px;
    font-size: 27px; font-weight: 300; color: var(--brand-blue); letter-spacing: 0.3px;
  }

  .legend {
    position: absolute; left: 444px; top: 251px;
    display: flex; gap: 38px; font-size: 12.5px;
  }
  .legend__item { display: flex; align-items: center; gap: 6px; }

  .dot { width: 10px; height: 10px; border-radius: 50%; display: inline-block; }
  .dot--ok { background: var(--ok); }
  .dot--alert { background: var(--alert); }

  .caption {
    height: 20px; font-size: 12.5px; padding-left: 8px;
    border-bottom: 1.5px solid var(--rule); line-height: 19px;
  }
  .row { height: 24px; display: flex; align-items: center; border-bottom: 1.5px solid var(--rule); font-size: 12.5px; }

  .info { position: absolute; left: 60px; top: 279px; width: 363px; }
  .info .row span:first-child { width: 152px; padding-left: 8px; }

  .results { position: absolute; left: 444px; top: 279px; width: 343px; }
  .results .caption { padding-left: 12px; }
  .results .row > * { flex: none; }
  .results .col-dot { width: 34px; padding-left: 5px; }
  .results .col-name { width: 86px; }
  .results .col-value { width: 38px; font-weight: 700; color: var(--ink-strong); }
  .results .col-range { width: 92px; }
  .results .col-unit { width: 93px; }
  .results .row--head { height: 22px; font-size: 11px; }
  .results .row--head .col-value { font-weight: 400; color: var(--ink); }
  sup { font-size: 8px; }
</style>
</head>
<body>
  <div class="band band--top" role="img" aria-label="Abstract header band of soft cyan, lilac, blue and green translucent shapes"></div>

  <div class="brand"><span class="brand__dot"></span><span>CoralPathway</span></div>

  <h1 class="title">DOCTOR'S SUMMARY</h1>

  <div class="legend">
    <span class="legend__item"><span class="dot dot--ok"></span>normal</span>
    <span class="legend__item"><span class="dot dot--alert"></span>abnormal</span>
  </div>

  <section class="info">
    <div class="caption">INFORMATION</div>
    <div class="row"><span>Patient name</span><span>Rohan Mehra</span></div>
    <div class="row"><span>Accession no</span><span>002MF095237</span></div>
    <div class="row"><span>Gender</span><span>male</span></div>
    <div class="row"><span>Age</span><span>49 years</span></div>
    <div class="row"><span>Drawn</span><span>14.08.2018</span></div>
    <div class="row"><span>Recieved</span><span>14.08.2018</span></div>
    <div class="row"><span>Reported</span><span>14.08.2018</span></div>
  </section>

  <section class="results">
    <div class="caption">TEST RESULTS</div>
    <div class="row row--head"><span class="col-dot"></span><span class="col-name">Test name</span><span class="col-value">Value</span><span class="col-range">Reference range</span><span class="col-unit">Unit</span></div>
    <div class="row"><span class="col-dot"><span class="dot dot--ok"></span></span><span class="col-name">Glucose</span><span class="col-value">78</span><span class="col-range">60-99</span><span class="col-unit">mg/dl</span></div>
    <div class="row"><span class="col-dot"><span class="dot dot--ok"></span></span><span class="col-name">CRP</span><span class="col-value">1.2</span><span class="col-range">&lt;5</span><span class="col-unit">mg/l</span></div>
    <div class="row"><span class="col-dot"><span class="dot dot--ok"></span></span><span class="col-name">Sodium</span><span class="col-value">142</span><span class="col-range">136-146</span><span class="col-unit">mmol/l</span></div>
    <div class="row"><span class="col-dot"><span class="dot dot--alert"></span></span><span class="col-name">Potassium</span><span class="col-value">5.2</span><span class="col-range">3.5-5.1</span><span class="col-unit">mmol/l</span></div>
    <div class="row"><span class="col-dot"><span class="dot dot--ok"></span></span><span class="col-name">Creatinine</span><span class="col-value">1.1</span><span class="col-range">0.7-1.2</span><span class="col-unit">mg/dl</span></div>
    <div class="row"><span class="col-dot"><span class="dot dot--ok"></span></span><span class="col-name">EGFR</span><span class="col-value">98</span><span class="col-range">&gt;60</span><span class="col-unit">ml/min/1.73 m<sup>2</sup></span></div>
    <div class="row"><span class="col-dot"><span class="dot dot--ok"></span></span><span class="col-name">Cholesterol</span><span class="col-value">120</span><span class="col-range">&lt;200</span><span class="col-unit">mg/dl</span></div>
    <div class="row"><span class="col-dot"><span class="dot dot--ok"></span></span><span class="col-name">Triglycerides</span><span class="col-value">97</span><span class="col-range">&lt;150</span><span class="col-unit">mg/dl</span></div>
    <div class="row"><span class="col-dot"><span class="dot dot--alert"></span></span><span class="col-name">ALT</span><span class="col-value">49</span><span class="col-range">&lt;41</span><span class="col-unit">U/l</span></div>
    <div class="row"><span class="col-dot"><span class="dot dot--ok"></span></span><span class="col-name">AST</span><span class="col-value">28</span><span class="col-range">&lt;38</span><span class="col-unit">U/l</span></div>
  </section>

  <div class="band band--bottom" role="img" aria-label="Abstract footer band of soft green, blue, lilac and cyan translucent shapes"></div>
</body>
</html>
```